Meadowlark Learning Growth Partners (MLGP)

This is a professional business card. Logo and picture are a must on the front of the card. I am an educational consultant. I have been consulting for the past three years for a company. I am now opening my own company. My goal for my consulting company is to eventually consult all over America.

Target Market(s)

Educators, schools, professionals

Industry/Entity Type

Consulting

Contact Information for Business Card

Picture/logo on front, simple modern design

Font styles to use
Serif

Colors
85abd2
0355a3
3176b5
cedeed

Requirements
Must have
• picture, logo,
• Odessa Pruitt, Ed.S
• address 5073 Cormorant ridge Dr. Nashville, TN 37940
• Cell:616-555-0148
• Office: 629-555-0172
• www.Mlgpedu.example
• pruittodessa@mailbox.example

```html
<!DOCTYPE html>
<html lang="en">
<head>
<meta charset="utf-8">
<title>Meadowlark Learning Growth Partners – Business Card</title>
<link href="https://fonts.googleapis.com/css2?family=Exo+2:wght@400;500;700;800&display=swap" rel="stylesheet">
<style>
  :root {
    --navy: #043673;
    --white: #ffffff;
    --ink: #3a3a3a;
    --muted: #8a8a8a;
    --stripe: #8d8d8d;
    --backdrop: #e6e3df;
    --photo-top: #4a7fc4;
    --photo-bottom: #2f3440;
  }
  * { box-sizing: border-box; margin: 0; padding: 0; }
  html, body { width: 1200px; height: 848px; overflow: hidden; }
  body {
    position: relative;
    background: var(--backdrop);
    font-family: "Exo 2", sans-serif;
  }
  .card {
    position: absolute;
    left: 262px;
    width: 652px;
    height: 354px;
    overflow: hidden;
    box-shadow: 0 6px 14px rgba(0,0,0,0.25);
  }
  /* Front */
  .card-front { top: 46px; background: var(--navy); color: var(--white); }
  .front-brand {
    position: absolute;
    left: 112px; top: 126px;
    display: flex; align-items: center;
  }
  .front-mark {
    font-size: 44px; font-weight: 700; letter-spacing: 4px;
    padding-right: 16px;
  }
  .front-divider { width: 1.5px; height: 92px; background: var(--white); }
  .front-name {
    padding-left: 16px;
    font-size: 21px; font-weight: 700; line-height: 25px;
  }
  .front-footer {
    position: absolute; left: 0; width: 100%; top: 315px;
    display: flex; justify-content: center; align-items: center; gap: 8px;
    font-size: 13px; letter-spacing: 5px;
  }
  .front-footer .rule { width: 70px; height: 1px; background: rgba(255,255,255,0.8); }
  /* Back */
  .card-back { top: 446px; background: var(--white); }
  .back-mark {
    position: absolute; left: 42px; top: 136px;
    font-size: 44px; line-height: 44px; font-weight: 800; letter-spacing: 3px; color: var(--navy);
  }
  .back-photo {
    position: absolute; left: 520px; top: 27px;
    width: 96px; height: 119px;
    background: linear-gradient(180deg, var(--photo-top) 0%, var(--photo-top) 55%, var(--photo-bottom) 100%);
  }
  .back-person {
    position: absolute; right: 36px; top: 196px; text-align: right;
  }
  .person-name { font-size: 19px; font-weight: 700; color: var(--navy); }
  .person-role { font-size: 13px; color: var(--muted); margin-top: 1px; }
  .edge-tab {
    position: absolute; right: 0; top: 199px; width: 7px; height: 32px; background: var(--navy);
  }
  .back-contact {
    position: absolute; left: 40px; top: 214px;
    font-size: 14px; color: var(--ink); line-height: 18px;
  }
  .address { margin-bottom: 9px; }
  .contact-line { display: flex; align-items: center; gap: 4px; }
  .contact-line svg { width: 12px; height: 12px; fill: var(--navy); flex: none; }
  .back-wave { position: absolute; left: 0; bottom: 0; width: 652px; height: 52px; }
  .back-url {
    position: absolute; left: 446px; top: 331px;
    font-size: 14px; line-height: 16px; color: var(--white); letter-spacing: 0.4px;
  }
</style>
</head>
<body>
  <section class="card card-front">
    <div class="front-brand">
      <div class="front-mark">MLGP</div>
      <div class="front-divider"></div>
      <div class="front-name">Meadowlark<br>Learning<br>Growth<br>Partners</div>
    </div>
    <div class="front-footer">
      <span class="rule"></span><span>www.Mlgpedu.example</span><span class="rule"></span>
    </div>
  </section>

  <section class="card card-back">
    <div class="back-mark">MLGP</div>
    <div class="back-photo" role="img" aria-label="Portrait photo of Odessa Pruitt"></div>
    <div class="back-person">
      <div class="person-name">Odessa Pruitt, Ed.S</div>
      <div class="person-role">Owner</div>
    </div>
    <div class="edge-tab"></div>
    <div class="back-contact">
      <div class="address">5073 Cormorant ridge<br>Dr. Nashville, TN 37940</div>
      <div class="contact-line">
        <svg viewBox="0 0 24 24"><path d="M6.6 10.8a15 15 0 0 0 6.6 6.6l2.2-2.2c.3-.3.7-.4 1-.2 1.1.4 2.3.6 3.6.6.6 0 1 .4 1 1V20c0 .6-.4 1-1 1A17 17 0 0 1 3 4c0-.6.4-1 1-1h3.5c.6 0 1 .4 1 1 0 1.3.2 2.5.6 3.6.1.3 0 .7-.2 1z"/></svg>
        <span>629-555-0172</span>
      </div>
      <div class="contact-line">
        <svg viewBox="0 0 24 24"><path d="M7 1h10a2 2 0 0 1 2 2v18a2 2 0 0 1-2 2H7a2 2 0 0 1-2-2V3a2 2 0 0 1 2-2zm0 3v14h10V4z"/></svg>
        <span>616-555-0148</span>
      </div>
      <div class="contact-line">
        <svg viewBox="0 0 24 24"><path d="M2 5h20v14H2zm2 2v.5l8 5 8-5V7zm0 2.8V17h16V9.8l-8 5z"/></svg>
        <span>pruittodessa@mailbox.example</span>
      </div>
    </div>
    <svg class="back-wave" viewBox="0 0 652 52" preserveAspectRatio="none" aria-hidden="true">
      <path d="M0 24 C160 46 300 36 440 14 C530 2 610 0 652 6 L652 16 C610 10 530 12 440 22 C300 44 160 54 0 36 Z" fill="var(--stripe)"/>
      <path d="M0 42 C160 56 300 46 440 27 C530 16 610 15 652 21 L652 52 L0 52 Z" fill="var(--navy)"/>
    </svg>
    <div class="back-url">www.Mlgpedu.example</div>
  </section>
</body>
</html>
```